Latvian local photo material wholesaler requires a Car Wrap Design for self-advertising

Car Wrap Design for Photo Materials Department

Design a captivating car wrap for our "white Dorvel Tanix 2020" that represents our photo materials department. We specialize in photo frames, albums, films, chemicals, and batteries, serving Latvian customers as a wholesaler. Our goal is to expand our reach to the Baltic States as well.

The design should be eye-catching and attention-grabbing, aimed at attracting bystanders. Please incorporate our logo into the wrap design if possible. Additionally, feel free to include a slogan related to providing clients with all their photo product needs.

For inspiration, visit our website [https://trenvik.lv/en/] to understand our business and explore our photo products [https://trenvik.lv/en/kategorijas/photo-materials/].

You can search for our photo department products here: https://ecom.trenvik.lv/ecom/
Under "Photo Goods" which is located to the left side of the screen under "Categories". Picture quality might not be the best and some of the products might not have images, but it's to get the general idea.

Please note that the car wrap design should be "standalone" and focused specifically on our photo department.
Updates

Low designer entries for the paid expectation (50+). As this is the first time trying out the service, just now noticed the option to "guarantee the project", by agreeing that there won't be a refund. Please extend the project deadline, so that there is enough time for designers to submit their ideas. Thank you.

Target Market(s)

Target market are everyday customers. B2C oriented business

Font styles to use
Other font styles liked:
• Josefin Sans

Requirements
Must have
• Products that we sell (they don't have to be the exact ones, but just to show the idea what we sell): photo frames, albums, films (+ nice to have chemicals, batteries)
Nice to have
• A place where our products are listed.
Should not have
• Logo names of products, that we are not partnered with. Partners here: https://trenvik.lv/en/about-us/

```html
<!DOCTYPE html>
<html lang="en">
<head>
<meta charset="utf-8">
<title>Trenvik photo materials – vehicle wrap, both sides</title>
<link rel="stylesheet" href="https://fonts.googleapis.com/css2?family=Montserrat:wght@500;700&display=swap">
<style>
  :root {
    --wrap-maroon: #8b2f35;
    --wrap-white: #ffffff;
    --page-bg: #f1f2f3;
    --panel-bg: #ffffff;
    --list-ink: #111111;
  }
  html, body {
    margin: 0;
    padding: 0;
    width: 990px;
    height: 1200px;
    overflow: hidden;
    background: var(--page-bg);
    font-family: "Montserrat", Arial, sans-serif;
  }
  .wrap-sheet {
    width: 990px;
    height: 1200px;
    display: flex;
    flex-direction: column;
    gap: 23px;
  }
  .wrap-side {
    display: block;
    width: 990px;
    height: 587px;
    background: var(--panel-bg);
  }
  .fill-maroon { fill: var(--wrap-maroon); }
  .fill-white { fill: var(--wrap-white); }
  .line-white { fill: none; stroke: var(--wrap-white); stroke-width: 4; }
  .line-maroon { fill: none; stroke: var(--wrap-maroon); stroke-width: 4; }
  .product-list-item {
    font-family: "Montserrat", Arial, sans-serif;
    font-weight: 700;
    font-size: 13.5px;
    fill: var(--list-ink);
  }
  .brand-name {
    font-family: "Montserrat", Arial, sans-serif;
    font-weight: 500;
  }
  .brand-name--panel { font-size: 24px; letter-spacing: 12px; }
  .brand-name--body { font-size: 24px; letter-spacing: 14px; }
  .contact-line {
    font-family: "Montserrat", Arial, sans-serif;
    font-weight: 700;
  }
  .product-label {
    font-family: "Montserrat", Arial, sans-serif;
    font-weight: 700;
    font-size: 17px;
    fill: var(--wrap-white);
  }
</style>
</head>
<body>
<main class="wrap-sheet">

  <!-- Passenger side -->
  <svg class="wrap-side wrap-side--right" viewBox="0 0 1736 1030" xmlns="http://www.w3.org/2000/svg">
    <polygon class="fill-maroon main-panel" points="985,450 1365,440 1262,705 555,727 555,520 650,520 650,545 980,525"/>
    <polygon class="fill-white product-card" points="500,605 975,530 980,695 555,718"/>
    <rect class="fill-maroon badge-square" x="565" y="518" width="85" height="100"/>
    <rect class="line-white" x="575" y="530" width="65" height="78"/>
    <g role="img" aria-label="Film strip decoration">
      <polygon class="fill-maroon" points="670,520 855,482 865,530 680,565"/>
    </g>

    <g class="product-list">
      <circle class="fill-maroon" cx="666" cy="597" r="6"/>
      <text class="product-list-item" x="676" y="601" transform="rotate(-7 676 601)">PHOTO ALBUMS</text>
      <circle class="fill-maroon" cx="814" cy="579" r="6"/>
      <text class="product-list-item" x="824" y="583" transform="rotate(-7 824 583)">PHOTO FRAMES</text>
      <circle class="fill-maroon" cx="671" cy="623" r="6"/>
      <text class="product-list-item" x="683" y="627" transform="rotate(-7 683 627)">PHOTO FRAME MOUNTS</text>
      <circle class="fill-maroon" cx="883" cy="597" r="6"/>
      <text class="product-list-item" x="892" y="601" transform="rotate(-7 892 601)">BATTERIES</text>
      <circle class="fill-maroon" cx="675" cy="650" r="6"/>
      <text class="product-list-item" x="686" y="654" transform="rotate(-7 686 654)">PHOTO PAPER</text>
      <circle class="fill-maroon" cx="821" cy="632" r="6"/>
      <text class="product-list-item" x="832" y="636" transform="rotate(-7 832 636)">PHOTO FILMS</text>
      <circle class="fill-maroon" cx="679" cy="677" r="6"/>
      <text class="product-list-item" x="690" y="681" transform="rotate(-7 690 681)">PHOTOCHEMISTRY</text>
      <circle class="fill-maroon" cx="684" cy="705" r="6"/>
      <text class="product-list-item" x="694" y="709" transform="rotate(-7 694 709)">DISPOSABLE CAMERAS</text>
    </g>

    <g class="brand-lockup">
      <rect class="line-white" x="1021" y="476" width="50" height="62"/>
      <text class="brand-name brand-name--panel fill-white" x="1098" y="516">TRENVIK</text>
    </g>
    <g class="contact-block">
      <text class="contact-line fill-white" x="1020" y="657" font-size="22">https://trenvik.lv/en/</text>
      <text class="contact-line fill-white" x="1020" y="690" font-size="22">(+371) 60 400 118</text>
    </g>
  </svg>

  <!-- Driver side -->
  <svg class="wrap-side wrap-side--left" viewBox="0 0 1736 1030" xmlns="http://www.w3.org/2000/svg">
    <g role="img" aria-label="Film strip decoration running along the rear">
      <polygon class="fill-maroon" points="95,560 420,545 420,560 100,575"/>
      <polygon class="fill-maroon" points="80,600 200,640 195,655 75,615"/>
      <polygon class="fill-maroon" points="470,660 600,770 585,780 460,675"/>
    </g>
    <polygon class="fill-maroon main-panel" points="370,440 740,453 755,527 1230,600 1190,720 600,722 470,722 430,560"/>

    <g class="brand-lockup">
      <rect class="line-maroon" x="865" y="475" width="55" height="70"/>
      <text class="brand-name brand-name--body fill-maroon" x="960" y="532" transform="rotate(6 960 532)">TRENVIK</text>
    </g>
    <g class="contact-block">
      <text class="contact-line fill-maroon" x="228" y="502" font-size="15">https://trenvik.lv/en/</text>
      <text class="contact-line fill-maroon" x="242" y="522" font-size="15">(+371) 60 400 118</text>
    </g>

    <g class="product-grid">
      <rect class="line-white" x="428" y="461" width="40" height="40"/>
      <rect class="line-white" x="436" y="469" width="24" height="24" stroke-width="2"/>
      <text class="product-label" x="480" y="477">PHOTO</text>
      <text class="product-label" x="480" y="497">ALBUMS</text>

      <rect class="line-white" x="599" y="498" width="44" height="36" stroke-width="3"/>
      <circle class="line-white" cx="621" cy="516" r="8" stroke-width="3"/>
      <text class="product-label" x="655" y="512">PHOTO</text>
      <text class="product-label" x="655" y="532">FRAMES</text>

      <circle class="line-white" cx="525" cy="588" r="14" stroke-width="3"/>
      <rect class="fill-white" x="483" y="572" width="10" height="34" transform="rotate(30 488 589)"/>
      <text class="product-label" x="556" y="585">PHOTO</text>
      <text class="product-label" x="556" y="605">FILMS</text>

      <circle class="line-white" cx="748" cy="582" r="12" stroke-width="3"/>
      <rect class="fill-white" x="732" y="593" width="40" height="8" rx="4"/>
      <text class="product-label" x="785" y="585">PHOTO</text>
      <text class="product-label" x="785" y="605">PAPER</text>

      <rect class="line-white" x="940" y="597" width="54" height="38" rx="4" stroke-width="3"/>
      <circle class="line-white" cx="967" cy="616" r="10" stroke-width="3"/>
      <text class="product-label" x="1012" y="614">DISPOSABLE</text>
      <text class="product-label" x="1012" y="634">CAMERAS</text>

      <rect class="fill-white" x="572" y="645" width="42" height="42"/>
      <rect class="fill-maroon" x="580" y="653" width="26" height="26"/>
      <text class="product-label" x="627" y="660">PHOTO FRAME</text>
      <text class="product-label" x="627" y="680">MOUNTS</text>

      <path class="line-white" stroke-width="3" d="M808,648 L808,668 L796,690 L834,690 L822,668 L822,648 Z"/>
      <text class="product-label" x="847" y="668">PHOTO</text>
      <text class="product-label" x="847" y="688">CHEMISTRY</text>

      <rect class="line-white" x="1050" y="672" width="20" height="36" rx="3" stroke-width="3" transform="rotate(20 1060 690)"/>
      <text class="product-label" x="1087" y="704">BATTERIES</text>
    </g>
  </svg>

</main>
</body>
</html>
```